Organic Food company needs a new design label logo

Our company name is Brackwell Dene Organic. We pack organic dried products and sell to natural, organic or small supermarkets in the UK.

We would like to you to design our new label with logo.

The label size should be the width is 65 mm and the length is 85 mm. The label should also include our land stewardship guild and European organic logos.

The food label should reflect our company that we are organic and we sell quality organic food products.

The colours should be pastel and warm colour. It shouldn’t have so many colour.
Updates

Dear All,

Just let you know that this project is food label with the new design. The size of the label should as follow; 
width: 65 mm
length: 85 mm

It will be used for dried fruit, vegetables and nuts. so the middle of the label should be blank, as the print shop will print the name separetly.

When you design our new logo label, please also read my previous note.

Thank you.

Target Market(s)

Above 25 years old. People who like to buy organic or natural food products. Middle income people.

Industry/Entity Type

It Company

Requirements
Must have
• 1) Land Stewardship Guild logo (attached as file )

2) European organic logo ( can be download from http://farmmark-register.example/produce/natural/seal-policy/badge_en )

3) The following information should be either next to or underneath to European logo;
XK-CRT-17
Non-EU Agriculture

The above text information shouldn't be very big.

4) There should be enough space in the middle of the label to write (later by the print shop) full product name and weight.

5) Our company name is "Brackwell Dene Organic"

6) Our web site address is www.brackwelldene.example

```html
<!DOCTYPE html>
<html lang="en">
<head>
<meta charset="utf-8">
<title>Brackwell Dene Organic – Product Labels</title>
<link rel="stylesheet" href="https://fonts.googleapis.com/css2?family=Fira+Sans+Condensed:wght@400;600&family=Allura&family=Open+Sans:wght@400&display=swap">
<style>
  :root {
    --canvas: #ffffff;
    --label-bg: #070707;
    --label-edge: #2a2a2a;
    --ink-light: #f2f2f2;
    --tone-sun: #f7b21c;
    --tone-amber: #f08522;
    --tone-wheat: #d6b370;
    --badge-green: #8dc63f;
    --badge-text: #e6e6e6;
    --seal-ring: #e8e8e8;
  }
  * { box-sizing: border-box; margin: 0; padding: 0; }
  html, body {
    width: 1200px;
    height: 920px;
    overflow: hidden;
    background: var(--canvas);
  }
  .label-sheet {
    width: 1200px;
    height: 920px;
    display: flex;
    justify-content: center;
    align-items: center;
    gap: 24px;
  }
  .label {
    position: relative;
    width: 330px;
    height: 432px;
    background: var(--label-bg);
    border: 2px solid var(--label-edge);
    border-radius: 10px;
    color: var(--brand-tone);
  }
  .label--sun { --brand-tone: var(--tone-sun); }
  .label--amber { --brand-tone: var(--tone-amber); }
  .label--wheat { --brand-tone: var(--tone-wheat); }

  .brand {
    position: absolute;
    top: 118px;
    left: 0;
    right: 0;
    text-align: center;
  }
  .brand__dot {
    display: block;
    width: 56px;
    height: 56px;
    margin: 0 auto 10px;
    border: 4px solid var(--brand-tone);
    border-radius: 50%;
  }
  .brand__name {
    font-family: "Fira Sans Condensed", sans-serif;
    font-weight: 600;
    color: var(--brand-tone);
    line-height: 1.02;
  }
  .brand__line { display: block; font-size: 36px; }
  .brand__line--sub { font-size: 28px; }

  .product-type {
    position: absolute;
    top: 290px;
    left: 0;
    right: 0;
    text-align: center;
    font-family: "Allura", cursive;
    font-size: 25px;
    color: var(--ink-light);
  }

  .label__footer {
    position: absolute;
    left: 26px;
    right: 18px;
    bottom: 18px;
    display: flex;
    align-items: flex-end;
  }
  .cert-eu {
    width: 54px;
    margin-right: 12px;
  }
  .cert-eu__mark {
    display: block;
    width: 54px;
    height: 34px;
    background: var(--badge-green);
  }
  .cert-eu__code {
    display: block;
    margin-top: 2px;
    font-family: "Open Sans", sans-serif;
    font-size: 8.5px;
    color: var(--badge-text);
    line-height: 1.05;
    white-space: nowrap;
  }
  .cert-eu__note {
    display: block;
    font-family: "Open Sans", sans-serif;
    font-size: 5px;
    color: var(--badge-text);
    white-space: nowrap;
  }
  .cert-guild {
    width: 46px;
    height: 46px;
    border: 2px solid var(--seal-ring);
    border-radius: 50%;
  }
  .web {
    margin-left: auto;
    margin-bottom: 14px;
    font-family: "Open Sans", sans-serif;
    font-size: 12.5px;
    color: var(--ink-light);
  }
</style>
</head>
<body>
  <main class="label-sheet">
    <article class="label label--sun">
      <div class="brand">
        <span class="brand__dot"></span>
        <h1 class="brand__name">
          <span class="brand__line">Brackwell Dene</span>
          <span class="brand__line brand__line--sub">Organic</span>
        </h1>
      </div>
      <p class="product-type">Dried Fruit</p>
      <footer class="label__footer">
        <div class="cert-eu">
          <span class="cert-eu__mark" role="img" aria-label="European organic certification badge"></span>
          <span class="cert-eu__code">XK-CRT-17</span>
          <span class="cert-eu__note">Non-EU Agriculture</span>
        </div>
        <span class="cert-guild" role="img" aria-label="Land Stewardship Guild organic seal"></span>
        <span class="web">www.brackwelldene.example</span>
      </footer>
    </article>

    <article class="label label--amber">
      <div class="brand">
        <span class="brand__dot"></span>
        <h1 class="brand__name">
          <span class="brand__line">Brackwell Dene</span>
          <span class="brand__line brand__line--sub">Organic</span>
        </h1>
      </div>
      <p class="product-type">Vegetable</p>
      <footer class="label__footer">
        <div class="cert-eu">
          <span class="cert-eu__mark" role="img" aria-label="European organic certification badge"></span>
          <span class="cert-eu__code">XK-CRT-17</span>
          <span class="cert-eu__note">Non-EU Agriculture</span>
        </div>
        <span class="cert-guild" role="img" aria-label="Land Stewardship Guild organic seal"></span>
        <span class="web">www.brackwelldene.example</span>
      </footer>
    </article>

    <article class="label label--wheat">
      <div class="brand">
        <span class="brand__dot"></span>
        <h1 class="brand__name">
          <span class="brand__line">Brackwell Dene</span>
          <span class="brand__line brand__line--sub">Organic</span>
        </h1>
      </div>
      <p class="product-type">Vegetable</p>
      <footer class="label__footer">
        <div class="cert-eu">
          <span class="cert-eu__mark" role="img" aria-label="European organic certification badge"></span>
          <span class="cert-eu__code">XK-CRT-17</span>
          <span class="cert-eu__note">Non-EU Agriculture</span>
        </div>
        <span class="cert-guild" role="img" aria-label="Land Stewardship Guild organic seal"></span>
        <span class="web">www.brackwelldene.example</span>
      </footer>
    </article>
  </main>
</body>
</html>
```